Business Card Design for an international medical business

We need a professional and elegant business card design with fashionable graphic element. Our company is located in Hong Kong with three worldwide production lines for medical equipment(surgical face masks, N95, face shields and so on). Our factories all contain medical standard ISOs and all product fulfill Garrow lab and KTR testing standards.

We would like to see designs that show the impression of our professional expertise, formal corporate image with creative thinking work style and inspiring global concept. We want the content in both English and Japanese on the same card. We also want to print our the patent trade mark and company logo on the card.

Target Market(s)

Southeast Asia, US, EU

Industry/Entity Type

Medical Equipment

Contact Information for Business Card

Below are the content we want to be shown on the business card(please help us to simplified them to be more presentable and readable):

Company name: Brightmoor (Hong Kong) 5K Medical Technology Company Limited
Address: Unit 2204, 22/F, Pine Court, No.8 Ferndale Road, Kwun Lam, Hong Kong.
Band Name: B5K
Homepage: www.brightmoor5kq.com
Name: Lok Wing Fei
Title: Manager
Tel: +852-xxxx-xxxx
Mobile: +852-xxxx-xxxx
Email: xx@brightmoor5kq.com

Production Lines:
China: Ping Shan Kai Lok Medical Technology Company Limited
Mo Tan City Ren Bo Textile Machinery Company Limited
Bangladesh: B5K Medical Technology Company Limited

Qualifications:
ISO 13485:2016
ISO 14644-1:2015
ISO Class 8 Cleanroom
ASTM F2100 Level 2
EN14683 Type IIR
EN149 FFP2
CE Certified
FDA Registration number: XXX

Requirements
Must have
• use pantone color for the design
and provide the pantone number for printing purpose
Should not have
• Background color should not be black.

```html
<!DOCTYPE html>
<html lang="en">
<head>
<meta charset="utf-8">
<title>B5K Business Card</title>
<link rel="stylesheet" href="https://fonts.googleapis.com/css2?family=Montserrat:wght@400;500;600;700&display=swap">
<style>
  :root {
    --red: #e0174a;
    --teal: #12a9ae;
    --ink: #2b2b2b;
    --card: #f1efee;
    --backdrop: #b3b3b3;
  }
  * { margin: 0; padding: 0; box-sizing: border-box; }
  html, body { width: 1200px; height: 982px; overflow: hidden; }
  body {
    background: var(--backdrop);
    font-family: "Montserrat", Arial, sans-serif;
    color: var(--ink);
    position: relative;
  }
  .card {
    position: absolute;
    top: 68px;
    width: 447px;
    height: 784px;
    background: var(--card);
    border-radius: 30px;
    overflow: hidden;
  }
  .card--front { left: 120px; }
  .card--back { left: 632px; }

  /* front */
  .brand-mark {
    position: absolute;
    left: 49px;
    top: 70px;
    display: flex;
    align-items: center;
    gap: 16px;
  }
  .brand-mark__dot {
    width: 34px; height: 34px; border-radius: 50%;
    background: var(--teal);
  }
  .brand-mark__name {
    font-size: 70px; font-weight: 700; color: var(--red);
    letter-spacing: 2px; line-height: 1;
  }
  .person { position: absolute; left: 48px; top: 303px; }
  .person__name {
    font-size: 36px; font-weight: 700; color: var(--red);
    line-height: 1; letter-spacing: 0.2px;
  }
  .person__title {
    font-size: 24px; font-weight: 400; color: var(--teal);
    margin-top: 8px; margin-left: 2px;
  }
  .divider {
    position: absolute; left: 49px; top: 411px;
    width: 43px; height: 4px; background: var(--red);
  }
  .address {
    position: absolute; left: 49px; top: 436px;
    font-size: 19.5px; line-height: 31.5px; font-style: normal;
  }
  .contacts { position: absolute; left: 49px; top: 552px; list-style: none; }
  .contacts li {
    display: flex; align-items: center; gap: 9px;
    height: 36px; font-size: 21.5px;
  }
  .contacts svg { width: 18px; height: 20px; flex: none; }

  /* back */
  .brand-line {
    position: absolute; left: 34px; top: 52px;
    display: flex; align-items: center; gap: 12px;
  }
  .brand-line__dot {
    width: 30px; height: 30px; border-radius: 50%; background: var(--teal);
  }
  .brand-line__rule { width: 2px; height: 56px; background: var(--teal); }
  .brand-line__name {
    font-size: 34px; font-weight: 700; color: var(--red);
    line-height: 1; letter-spacing: 0.5px;
  }
  .brand-line__tagline {
    font-size: 10.5px; font-weight: 600; color: var(--teal);
    margin-top: 6px; margin-left: 3px;
  }
  .section-title {
    font-size: 19px; font-weight: 600; color: var(--red); line-height: 1;
  }
  .production { position: absolute; left: 34px; top: 174px; }
  .production__entry {
    font-size: 18.5px; line-height: 28.5px; margin-top: 6px;
  }
  .production__entry + .production__entry { margin-top: 14px; }
  .production__region { color: var(--teal); font-weight: 600; }
  .qualifications { position: absolute; left: 34px; top: 430px; }
  .qualifications ul { list-style: none; margin-top: 6px; }
  .qualifications li {
    font-size: 19px; line-height: 31px; position: relative; padding-left: 17px;
  }
  .qualifications li::before {
    content: ""; position: absolute; left: 2px; top: 12px;
    width: 8px; height: 8px; border-radius: 50%; background: var(--red);
  }

  .wave { position: absolute; left: 0; bottom: 0; width: 447px; height: 80px; }
  .wave .red { fill: var(--red); }
  .wave .teal { fill: var(--teal); }
</style>
</head>
<body>

<section class="card card--front" aria-label="Business card front">
  <div class="brand-mark">
    <span class="brand-mark__dot"></span>
    <span class="brand-mark__name">B5K</span>
  </div>

  <div class="person">
    <h1 class="person__name">LOK WING FEI</h1>
    <p class="person__title">Manager</p>
  </div>
  <div class="divider"></div>

  <address class="address">
    Unit 2204, 22/F<br>
    Pine Court, No.8 Ferndale Road<br>
    Kwun Lam, Hong Kong
  </address>

  <ul class="contacts">
    <li>
      <svg viewBox="0 0 20 20" aria-hidden="true"><path fill="var(--red)" d="M4 2l3 0 2 5-2 1.5c1 2.2 2.5 3.8 4.5 4.5L13 11l5 2v3c0 1-1 2-2 2C9 18 2 11 2 4c0-1 1-2 2-2z"/><path fill="none" stroke="var(--red)" stroke-width="1.4" d="M12 3a5 5 0 0 1 5 5M12 6a2 2 0 0 1 2 2"/></svg>
      +852-0000-0000
    </li>
    <li>
      <svg viewBox="0 0 20 20" aria-hidden="true"><rect x="5" y="1" width="10" height="18" rx="2" fill="none" stroke="var(--red)" stroke-width="1.8"/><circle cx="10" cy="16" r="1" fill="var(--red)"/></svg>
      +852-4827-1930
    </li>
    <li>
      <svg viewBox="0 0 20 20" aria-hidden="true"><rect x="1" y="4" width="18" height="12" fill="var(--red)"/><path d="M1 4l9 7 9-7" fill="none" stroke="var(--card)" stroke-width="1.4"/></svg>
      info@brightmoor5kq.com
    </li>
    <li>
      <svg viewBox="0 0 20 20" aria-hidden="true"><circle cx="10" cy="10" r="8.5" fill="var(--red)"/><path d="M2 10h16M10 1.5c-3 3-3 14 0 17M10 1.5c3 3 3 14 0 17" fill="none" stroke="var(--card)" stroke-width="1.2"/></svg>
      www.brightmoor5kq.com
    </li>
  </ul>

  <svg class="wave" viewBox="0 0 447 80" aria-hidden="true">
    <path class="red" d="M0,46 C120,20 260,12 398,20 C260,18 120,40 0,68 Z"/>
    <path class="teal" d="M18,80 C150,50 300,42 447,58 L447,80 Z"/>
  </svg>
</section>

<section class="card card--back" aria-label="Business card back">
  <div class="brand-line">
    <span class="brand-line__dot"></span>
    <span class="brand-line__rule"></span>
    <div>
      <div class="brand-line__name">BRIGHTMOOR</div>
      <div class="brand-line__tagline">5K Medical Technology Company Limited</div>
    </div>
  </div>

  <div class="production">
    <h2 class="section-title">PRODUCTION LINES:</h2>
    <p class="production__entry"><span class="production__region">China:</span> Ping Shan Kai Lok<br>Medical Technology Company Limited</p>
    <p class="production__entry"><span class="production__region">Mo Tan City</span> Ren Bo<br>Textile Machinery Company Limited</p>
    <p class="production__entry"><span class="production__region">Bangladesh:</span> B5K Medical<br>Technology Company Limited</p>
  </div>

  <div class="qualifications">
    <h2 class="section-title">Qualifications:</h2>
    <ul>
      <li>ISO 13485:2016</li>
      <li>ISO 14644-1:2015</li>
      <li>ISO Class 8 Cleanroom</li>
      <li>ASTM F2100 Level 2</li>
      <li>EN14683 Type IIR</li>
      <li>EN149 FFP2</li>
      <li>CE Certified</li>
      <li>FDA Registration number: XXX</li>
    </ul>
  </div>

  <svg class="wave" viewBox="0 0 447 80" aria-hidden="true">
    <path class="red" d="M52,22 C200,10 350,16 447,38 L447,54 C330,32 200,24 52,22 Z"/>
    <path class="teal" d="M0,80 L0,62 C120,34 300,40 420,80 Z"/>
  </svg>
</section>

</body>
</html>
```